Real Estate Investment Company Needs Business Card Design

TurnKeyMintHomes is a real estate investment company that primarily deals directly with homeowners looking to sell their homes in "as is" condition as quick as possible. We give this seller cash and close on their nightmare of a property in just a matter of days.

Our logo is attached - (please keep logo in tact, use as is)

Industry/Entity Type

Real Estate

Contact Information for Business Card

The design should invoke trust & professionalism. The person holding the card should feel rest assured that we are the right company to work with.

Font styles to use
Sans Serif

Requirements
Must have
• Card must include "Call us today for a fair offer on your property so you can move on with your life!"
Nice to have
• If possible, include this either on front or back (you can use your own formatting, below is just the text)
• "
• No Realtor Commissions
• No Repairs To Deal With
• No Closing Costs "

```html
<!DOCTYPE html>
<html lang="en">
<head>
<meta charset="utf-8">
<title>TurnKeyMintHomes Business Card</title>
<link rel="stylesheet" href="https://fonts.googleapis.com/css2?family=Lato:wght@400;700;900&display=swap">
<style>
  :root {
    --page-bg: #d9dbde;
    --brand-blue: #3a8fd4;
    --brand-blue-deep: #2a76bd;
    --brand-blue-light: #4a9ee0;
    --name-blue: #2b7fc9;
    --paper-white: #ffffff;
    --paper-grey: #e6e7e9;
    --logo-pale: #dde3f3;
    --text-white: #ffffff;
  }
  * { box-sizing: border-box; margin: 0; padding: 0; }
  html, body {
    width: 1200px;
    height: 864px;
    overflow: hidden;
  }
  body {
    background: var(--page-bg);
    font-family: "Lato", Arial, sans-serif;
    display: flex;
    flex-direction: column;
    align-items: center;
    justify-content: center;
    gap: 44px;
  }
  .card {
    width: 600px;
    height: 343px;
    position: relative;
    overflow: hidden;
    box-shadow: 0 6px 18px rgba(0,0,0,0.18);
  }

  /* Back side */
  .card-back {
    background: radial-gradient(ellipse at 45% 45%, var(--brand-blue-light) 0%, var(--brand-blue) 50%, var(--brand-blue-deep) 100%);
    display: flex;
    flex-direction: column;
    align-items: center;
    justify-content: center;
    gap: 22px;
  }
  .card-back .brand-row {
    display: flex;
    align-items: center;
    gap: 14px;
  }
  .card-back .brand-dot {
    width: 22px;
    height: 22px;
    border-radius: 50%;
    background: var(--logo-pale);
  }
  .card-back .brand-name {
    color: var(--logo-pale);
    font-weight: 900;
    font-size: 44px;
    line-height: 52px;
    letter-spacing: 0.2px;
  }
  .card-back .call-to-action {
    max-width: 440px;
    text-align: center;
    color: var(--text-white);
    font-size: 17px;
    line-height: 24px;
    font-weight: 400;
  }

  /* Front side */
  .card-front {
    background: var(--brand-blue);
  }
  .card-front .top-band {
    position: absolute;
    left: 0; top: 0;
    width: 100%;
    height: 150px;
    background: linear-gradient(180deg, var(--paper-white) 0%, var(--paper-grey) 100%);
  }
  .card-front .brand-name {
    position: absolute;
    left: 0; top: 84px;
    width: 100%;
    text-align: center;
    color: var(--name-blue);
    font-weight: 900;
    font-size: 40px;
    line-height: 48px;
    letter-spacing: 0.2px;
  }
  .holder {
    position: absolute;
    left: 40px;
    top: 178px;
    width: 250px;
    text-align: right;
    color: var(--text-white);
  }
  .holder .person-name {
    font-size: 23px;
    font-weight: 700;
    line-height: 28px;
  }
  .holder .person-role,
  .holder .address-line {
    font-size: 16px;
    line-height: 21px;
  }
  .holder .address-block { margin-top: 4px; }
  .contacts {
    position: absolute;
    left: 322px;
    top: 190px;
    list-style: none;
    color: var(--text-white);
  }
  .contacts li {
    display: flex;
    align-items: center;
    gap: 9px;
    font-size: 17px;
    line-height: 25px;
  }
  .contacts .icon {
    width: 16px;
    height: 16px;
    flex: none;
  }
</style>
</head>
<body>

  <section class="card card-back" aria-label="Card back">
    <div class="brand-row">
      <span class="brand-dot"></span>
      <span class="brand-name">TurnKeyMintHomes</span>
    </div>
    <p class="call-to-action">Call us today for a fair offer on your property so you can move on with your life!</p>
  </section>

  <section class="card card-front" aria-label="Card front">
    <div class="top-band"></div>
    <div class="brand-name">TurnKeyMintHomes</div>

    <div class="holder">
      <div class="person-name">Daniel Reyes</div>
      <div class="person-role">Managing Director</div>
      <div class="address-block">
        <div class="address-line">1234, Address GoesHere</div>
        <div class="address-line">Country, 12345</div>
      </div>
    </div>

    <ul class="contacts">
      <li>
        <svg class="icon" viewBox="0 0 16 16" aria-hidden="true">
          <rect width="16" height="16" rx="3" fill="#fff"/>
          <path d="M3.5 6.5c0-1.5 2-2.5 4.5-2.5s4.5 1 4.5 2.5v.8h-2.3v-1H5.8v1H3.5z" fill="#2f6fb0"/>
          <rect x="4.5" y="8" width="7" height="4.5" rx="1" fill="#2f6fb0"/>
        </svg>
        <span>123-456-7890</span>
      </li>
      <li>
        <svg class="icon" viewBox="0 0 16 16" aria-hidden="true">
          <rect width="16" height="16" rx="3" fill="#fff"/>
          <rect x="5" y="2.5" width="6" height="11" rx="1.2" fill="#2f6fb0"/>
          <rect x="6" y="4" width="4" height="6" fill="#fff"/>
          <circle cx="8" cy="11.8" r="0.8" fill="#fff"/>
        </svg>
        <span>123-456-7890</span>
      </li>
      <li>
        <svg class="icon" viewBox="0 0 16 16" aria-hidden="true">
          <rect width="16" height="16" rx="3" fill="#fff"/>
          <rect x="3" y="4.5" width="10" height="7" fill="#2f6fb0"/>
          <path d="M3 4.5l5 4 5-4" fill="none" stroke="#fff" stroke-width="1"/>
        </svg>
        <span>info@youremail.com</span>
      </li>
      <li>
        <svg class="icon" viewBox="0 0 16 16" aria-hidden="true">
          <rect width="16" height="16" rx="3" fill="#fff"/>
          <path d="M6.5 9.5l3-3M7 5.5l1-1a2 2 0 0 1 3 3l-1 1M9 10.5l-1 1a2 2 0 0 1-3-3l1-1" fill="none" stroke="#2f6fb0" stroke-width="1.5" stroke-linecap="round"/>
        </svg>
        <span>www.yourweb.com</span>
      </li>
    </ul>
  </section>

</body>
</html>
```